Design für Wein-Etikett
Zielgruppe
Zielgruppe ist sowohl der traditionelle Weintrinker (der obendrein auf "Blaublütiges" steht), vor allem aber das junge, moderne Weinpublikum, welches die Message verstanden hat: "Traditionelles modern präsentiert".
Aufgabenstellung
Erstellung eines MODERNEN Weinflaschen-Etikettes, obwohl es auf der Tradition eines alten Prinzengeschlecht beruht. Das Etikett soll als Basis für eine künftige Weinlinie dienen, d.h. das Grundlayout bleibt bestehen, der Jahrgang, die Lagenbezeichnung, die Rebsorten und die AP-Nr. (Abfüllbetrieb) werden variieren.

```html
<!DOCTYPE html>
<html lang="de">
<head>
<meta charset="utf-8">
<title>Riesling – Edition Prinz von Hallenstein-Morburg</title>
<link rel="stylesheet" href="https://fonts.googleapis.com/css2?family=Libre+Baskerville:wght@400;700&display=swap">
<style>
  :root {
    --backdrop: #e9e9e9;
    --paper: #ffffff;
    --wine-green: #17793a;
    --wine-green-dark: #0f5e2b;
    --gold-text: #b3894a;
    --gold-light: #e3d2ad;
    --gold-mid: #cdb07c;
    --gold-deep: #bc9a62;
    --gold-faint: rgba(255, 255, 255, 0.18);
  }
  * { box-sizing: border-box; margin: 0; padding: 0; }
  html, body {
    width: 1200px;
    height: 1200px;
    overflow: hidden;
    background: var(--backdrop);
    font-family: "Libre Baskerville", "Times New Roman", serif;
  }
  .canvas {
    width: 1200px;
    height: 1200px;
    display: flex;
    align-items: center;
    justify-content: center;
  }
  .wine-label {
    width: 780px;
    height: 1000px;
    background: var(--paper);
    display: flex;
    flex-direction: column;
    box-shadow: 0 2px 14px rgba(0,0,0,0.08);
  }
  .top-rule {
    height: 14px;
    background: var(--wine-green);
    border-bottom: 4px solid var(--paper);
    box-shadow: 0 4px 0 var(--wine-green-dark);
  }
  .title-field {
    flex: 0 0 446px;
    display: flex;
    flex-direction: column;
    align-items: center;
    padding-top: 42px;
  }
  .house-mark {
    display: flex;
    align-items: center;
    gap: 12px;
    color: var(--gold-text);
    font-size: 30px;
    font-weight: 400;
    letter-spacing: 1px;
    height: 150px;
  }
  .house-mark .dot {
    width: 14px;
    height: 14px;
    border-radius: 50%;
    background: var(--gold-text);
  }
  .edition {
    margin-top: 18px;
    color: var(--gold-text);
    font-size: 26px;
    line-height: 1.35;
    text-align: center;
  }
  .variety {
    margin-top: 34px;
    color: var(--wine-green);
    font-size: 118px;
    font-weight: 700;
    letter-spacing: 2px;
    line-height: 1;
  }
  .gold-band {
    flex: 1;
    position: relative;
    background: linear-gradient(180deg, var(--gold-light) 0%, var(--gold-mid) 40%, var(--gold-deep) 100%);
    display: flex;
    align-items: center;
    justify-content: center;
    overflow: hidden;
  }
  .gold-band .faint-mark {
    color: var(--gold-faint);
    font-size: 96px;
    font-weight: 400;
    letter-spacing: 4px;
  }
  .footer-band {
    flex: 0 0 64px;
    background: var(--wine-green);
    border-top: 5px solid var(--paper);
    box-shadow: inset 0 5px 0 var(--wine-green-dark);
    display: flex;
    align-items: center;
    justify-content: center;
  }
  .web-address {
    color: #ffffff;
    font-size: 17px;
    letter-spacing: 0.5px;
  }
</style>
</head>
<body>
  <main class="canvas">
    <article class="wine-label">
      <div class="top-rule"></div>
      <header class="title-field">
        <div class="house-mark"><span class="dot"></span>Hallenstein</div>
        <p class="edition">Edition<br>Prinz von Hallenstein-Morburg</p>
        <h1 class="variety">RIESLING</h1>
      </header>
      <section class="gold-band">
        <span class="faint-mark">Hallenstein</span>
      </section>
      <footer class="footer-band">
        <span class="web-address">www.weinhaus-kronberg.de</span>
      </footer>
    </article>
  </main>
</body>
</html>
```